To design a look and feel for a website. The company offers technical services to governemtns and public bodies. It does NOT market to the public.

The core business is GIS (Geographic Information Systems)

The site needs to be clean and simple, The current version is available here: www.velda.ie

Target Market(s)

Goverment agencies and public bodies in the EU, buying through the public procurerment process

Requirements
Should not have
• corny graphics of hands holding globes or sateliites please.

```html
<!DOCTYPE html>
<html lang="en">
<head>
<meta charset="utf-8">
<title>Velda – Information Expertise</title>
<link rel="stylesheet" href="https://fonts.googleapis.com/css2?family=Roboto+Condensed:wght@400;700&family=Open+Sans:ital,wght@0,400;0,600;1,600&display=swap">
<style>
:root{
  --navy-deep:#03205a;
  --navy-dark:#0b1f5c;
  --navy:#1f3f85;
  --band:#213f7a;
  --title:#1a3170;
  --text:#444;
  --header-bg:#f7f7f7;
  --client-bg:#ececec;
  --footer:#111;
  --white:#fff;
}
*{margin:0;padding:0;box-sizing:border-box}
html,body{width:892px;height:1200px;overflow:hidden}
body{position:relative;background:var(--white);font-family:"Open Sans",sans-serif;color:var(--text)}
.section{position:absolute;left:0;width:892px}

/* header */
.site-header{top:0;height:106px;background:var(--header-bg)}
.brand{position:absolute;left:56px;top:36px;display:flex;align-items:center;gap:8px;font-family:"Roboto Condensed",sans-serif;font-weight:700;font-size:30px;line-height:1;color:var(--navy)}
.brand-mark{width:14px;height:14px;background:var(--navy)}
.main-nav{position:absolute;left:405px;top:35px;display:flex;height:36px}
.main-nav a{display:flex;align-items:center;justify-content:center;height:36px;background:var(--navy);color:var(--white);text-decoration:none;font-family:"Roboto Condensed",sans-serif;font-size:16px;margin-right:1px}
.main-nav a.active{background:var(--navy-dark)}

/* hero */
.hero{top:106px;height:322px;background:var(--navy-deep)}
.hero-copy{position:absolute;left:70px;top:106px;font-family:"Roboto Condensed",sans-serif;font-size:23px;line-height:31px;color:var(--white)}
.hero-dots{position:absolute;left:172px;top:238px;display:flex;gap:4px}
.hero-dots span{width:9px;height:9px;border-radius:50%;background:var(--white)}
.hero-dots span.on{background:#7a80c4}
.hero-art{position:absolute;left:430px;top:4px;width:410px;height:312px;background:radial-gradient(ellipse at 50% 40%,#2a6cff 0%,#1547c9 40%,#03205a 85%)}

/* welcome */
.welcome{top:428px;height:210px;text-align:center}
.welcome h1{margin-top:14px;font-family:"Roboto Condensed",sans-serif;font-weight:400;font-size:22px;color:var(--title)}
.rule{width:62px;height:2px;background:var(--title);margin:3px auto 8px}
.welcome p{width:790px;margin:0 auto 6px;font-size:10.4px;line-height:14px}
.btn{display:inline-block;margin-top:8px;padding:4px 8px;background:var(--navy-dark);color:var(--white);font-size:10.5px;text-decoration:none}

/* services */
.services{top:638px;height:367px;background:var(--band);color:var(--white)}
.services h2{text-align:center;margin-top:14px;font-family:"Roboto Condensed",sans-serif;font-size:19px;font-weight:700}
.service{position:absolute;width:235px}
.service svg{display:block;margin:0 auto;width:42px;height:40px;fill:var(--white)}
.service h3{text-align:center;font-family:"Roboto Condensed",sans-serif;font-size:19px;font-weight:700;margin-top:10px}
.service p{font-size:10.4px;line-height:16px;margin-top:4px;height:48px}
.more{display:block;text-align:right;padding-right:12px;font-size:9.5px;font-weight:600;font-style:italic;margin-top:6px}

/* clients */
.clients{top:1005px;height:156px}
.clients-bar{position:absolute;left:55px;top:25px;width:782px;height:31px;background:#e8e8e8;text-align:center}
.clients-bar h2{font-family:"Roboto Condensed",sans-serif;font-size:19px;font-weight:400;color:var(--title);line-height:31px}
.arrow{position:absolute;top:4px;width:21px;height:23px;display:flex;align-items:center;justify-content:center}
.arrow.prev{left:738px;background:#555}
.arrow.next{left:761px;background:var(--navy-dark)}
.arrow svg{width:8px;height:10px;stroke:var(--white);fill:none;stroke-width:2}
.client{position:absolute;top:61px;width:114px;height:82px;background:var(--client-bg);border-top:3px solid var(--navy-dark);box-shadow:0 6px 5px -4px rgba(0,0,0,.45);display:flex;align-items:center;justify-content:center;font-size:13px;font-weight:600;color:#444}

/* footer */
.site-footer{top:1161px;height:39px;background:var(--footer);font-size:10.4px;color:#999}
.footer-nav{position:absolute;left:55px;top:13px}
.footer-nav a{color:#999;text-decoration:none}
.footer-nav a.active{color:var(--white)}
.footer-nav i{font-style:normal;margin:0 6px}
.copyright{position:absolute;right:53px;top:13px}
</style>
</head>
<body>

<header class="section site-header">
  <div class="brand"><span class="brand-mark"></span>VELDA</div>
  <nav class="main-nav">
    <a class="active" href="#" style="width:73px">Home</a>
    <a href="#" style="width:96px">Services</a>
    <a href="#" style="width:85px">Clients</a>
    <a href="#" style="width:90px">Contact</a>
    <a href="#" style="width:84px;margin-right:0">INSPIRE</a>
  </nav>
</header>

<section class="section hero">
  <div class="hero-copy">We can help With Spaital vector Data<br>VELDA also has a strong Experise in<br>general data Mangagement</div>
  <div class="hero-dots"><span></span><span></span><span class="on"></span><span></span><span></span></div>
  <div class="hero-art" role="img" aria-label="Scattered large blue serif numerals glowing on a dark navy background"></div>
</section>

<section class="section welcome">
  <h1>Welcome to Velda.com</h1>
  <div class="rule"></div>
  <p>The VELDA Group has been in business since 1994 and continues to develop and update its range of services. The company has a high level of expertise in handling data and information, and in building and re-engineering database systems. We have a particular expertise in working with Irish data sets and have a strong grounding in dealing with spatial data.</p>
  <p>We also have extensive experience in working in a Northwind development environment, both Desktop and WebForge. We have worked on development of small scale systems using Northwind products for over 12 years. We have assisted in the migration of systems from Deskbase to both Sequel Store and Orrin DB databases. This has included re-writing code from MacroScript to either BasicNet or CoreScript.</p>
  <p>We have built web sites for our clients using WebForge using WebForge frameworks 1.5 through to 4.0.</p>
  <a class="btn" href="#">Read More</a>
</section>

<section class="section services">
  <h2>Our Service</h2>

  <div class="service" style="left:55px;top:47px">
    <svg viewBox="0 0 42 40"><path d="M6 2h30l4 8v28H2V10zM5 12v24h32V12zm3 3h26v8H8zm0 10h26v8H8zM18 18h6v2h-6zm0 10h6v2h-6z" fill-rule="evenodd"/></svg>
    <h3>Data Management</h3>
    <p>VELDA has extensive experience in Spatial Data processing. Services include:VELDA has extensive experience in Spatial Data processing.</p>
    <span class="more">Find Out More »</span>
  </div>

  <div class="service" style="left:334px;top:47px">
    <svg viewBox="0 0 42 40"><path d="M18 1h6l1 5 4 2 4-3 4 4-3 4 2 4 5 1v6l-5 1-2 4 3 4-4 4-4-3-4 2-1 5h-6l-1-5-4-2-4 3-4-4 3-4-2-4-5-1v-6l5-1 2-4-3-4 4-4 4 3 4-2zM21 11a9 9 0 1 0 .01 0zm0 5a4 4 0 1 1-.01 0z" fill-rule="evenodd"/></svg>
    <h3>Spatial Data</h3>
    <p>&nbsp;The rapid development of the use and availability of Spatial Data presents most organisations with opportunity.</p>
    <span class="more">Find Out More »</span>
  </div>

  <div class="service" style="left:608px;top:47px">
    <svg viewBox="0 0 42 40"><circle cx="20" cy="16" r="12"/><path d="M30 4a16 16 0 0 1-14 26" stroke="#fff" stroke-width="3" fill="none"/><path d="M19 30h3v5h6v3H13v-3h6z"/></svg>
    <h3>Land Use</h3>
    <p>&nbsp;The rapid development of the use and availability of Spatial Data presents most organisations with opportunity.</p>
    <span class="more">Find Out More »</span>
  </div>

  <div class="service" style="left:55px;top:210px">
    <svg viewBox="0 0 42 40"><path d="M16 4h26v26H16zM3 14h11v16H1V20zm3 3l-2 4h8v-4z" fill-rule="evenodd"/><circle cx="9" cy="32" r="5"/><circle cx="33" cy="32" r="5"/></svg>
    <h3>Transport</h3>
    <p>VELDA offers advice on route management and fleet asset tracking with EMC reporting</p>
    <span class="more">Find Out More »</span>
  </div>

  <div class="service" style="left:334px;top:210px">
    <svg viewBox="0 0 42 40"><circle cx="21" cy="10" r="7"/><circle cx="9" cy="15" r="5"/><circle cx="33" cy="15" r="5"/><path d="M10 36c0-12 4-17 11-17s11 5 11 17zM1 36c0-9 3-13 8-13 2 0 3 1 4 2-3 3-4 7-4 11zm40 0c0-9-3-13-8-13-2 0-3 1-4 2 3 3 4 7 4 11z"/></svg>
    <h3>Consulting</h3>
    <p>VELDA has extensive experience in Spatial Data processing. Services include:VELDA has extensive experience in Spatial Data processing.</p>
    <span class="more">Find Out More »</span>
  </div>

  <div class="service" style="left:608px;top:210px">
    <svg viewBox="0 0 42 40"><path d="M2 6h12l3 4h20v4H8L4 34H2zM9 16h32l-5 20H4z"/></svg>
    <h3>Databases</h3>
    <p>VELDA has extensive experience in Spatial Data processing. Services include:VELDA has extensive experience in Spatial Data processing.</p>
    <span class="more">Find Out More »</span>
  </div>
</section>

<section class="section clients">
  <div class="clients-bar">
    <h2>Some of Our Clients</h2>
    <span class="arrow prev"><svg viewBox="0 0 8 10"><path d="M6 1L2 5l4 4"/></svg></span>
    <span class="arrow next"><svg viewBox="0 0 8 10"><path d="M2 1l4 4-4 4"/></svg></span>
  </div>
  <div class="client" style="left:63px">Coach Ardmore</div>
  <div class="client" style="left:193px">Nations Forum</div>
  <div class="client" style="left:323px">Harp Registry</div>
  <div class="client" style="left:453px">Liffey Transit</div>
  <div class="client" style="left:583px">Statona</div>
  <div class="client" style="left:713px">Kestrel Fund</div>
</section>

<footer class="section site-footer">
  <nav class="footer-nav">
    <a class="active" href="#">Home</a><i>|</i><a href="#">Services</a><i>|</i><a href="#">Clients</a><i>|</i><a href="#">Contact</a><i>|</i><a href="#">INSPIRE</a>
  </nav>
  <div class="copyright">Copyright 2013 VELDA. All rights reserved</div>
</footer>

</body>
</html>
```